Business card and stationary for consulting business

We need business cards and matching stationary for professional consulting business for employment and human resources issues.
One of the CraftHive designers designed the logo with our company name.  Use the colors in the logo and may use light yellow as an accent color.
Add
Mara T. Vollen, J.D., LL.M.
485 E. Callister Lane
Winter Park, Florida  32789
407-555-0183
maravollenjd@quillpost.example

Industry/Entity Type
Business

```html
<!DOCTYPE html>
<html lang="en">
<head>
<meta charset="utf-8">
<title>Northgate HR — Business Card</title>
<link rel="stylesheet" href="https://fonts.googleapis.com/css2?family=Arvo:wght@700&family=Lato:ital,wght@0,400;0,900;1,400&display=swap">
<style>
  :root {
    --stage: #3b2a20;
    --card-yellow: #ffcc00;
    --card-yellow-light: #ffd84a;
    --bubble-blue: #2aaae2;
    --bubble-blue-dark: #1b7fb0;
    --ink-blue: #1a6a98;
    --accent-blue: #3aa6dd;
    --note-ink: #3f3f40;
    --note-text: #23415a;
    --paper: #f6f1de;
  }
  * { box-sizing: border-box; margin: 0; padding: 0; }
  html, body { width: 1200px; height: 1080px; overflow: hidden; }
  body {
    background: var(--stage);
    position: relative;
    font-family: "Lato", sans-serif;
  }
  .card {
    position: absolute;
    width: 700px;
    height: 405px;
    background: var(--card-yellow);
    box-shadow: 0 12px 30px rgba(0,0,0,.35);
    overflow: hidden;
  }
  .card--front { left: 80px; top: 70px; }
  .card--back { left: 420px; top: 590px; }

  /* Front */
  .brand { position: absolute; left: 34px; top: 30px; }
  .brand__name {
    font-weight: 400;
    font-size: 44px;
    line-height: 1;
    color: var(--ink-blue);
    letter-spacing: .5px;
  }
  .brand__tagline {
    margin-top: 4px;
    font-size: 10.5px;
    color: var(--ink-blue);
    letter-spacing: .2px;
  }
  .greeting {
    position: absolute;
    left: 83px; top: 108px;
    width: 537px; height: 150px;
  }
  .greeting__bubble { position: absolute; inset: 0; overflow: visible; }
  .greeting__text {
    position: relative;
    height: 140px;
    display: flex; align-items: center; justify-content: center;
    font-family: "Arvo", serif;
    font-weight: 700;
    font-size: 33px;
    color: #fff;
  }
  .holder { position: absolute; left: 188px; top: 292px; }
  .holder__name {
    font-weight: 900;
    font-size: 37px;
    color: var(--ink-blue);
    line-height: 1;
  }
  .holder__credentials {
    text-align: right;
    font-style: italic;
    font-size: 13px;
    color: var(--accent-blue);
    margin-top: 2px;
  }

  /* Back */
  .mark-ghost {
    position: absolute;
    right: 20px; top: 150px;
    width: 260px; height: 230px;
    background: var(--card-yellow-light);
    opacity: .7;
  }
  .contact-note {
    position: absolute;
    left: 66px; top: 100px;
    width: 285px; height: 285px;
  }
  .contact-note__sheet { position: absolute; inset: 0; }
  .contact-note__body { position: relative; padding: 52px 28px 0 32px; }
  .contact-note__title {
    font-family: "Arvo", serif;
    font-weight: 700;
    font-size: 30px;
    color: var(--note-ink);
    margin-bottom: 36px;
  }
  .contact-list { list-style: none; }
  .contact-list li {
    display: flex; align-items: flex-start; gap: 10px;
    font-size: 11.5px; line-height: 1.4;
    color: var(--note-text);
    margin-bottom: 14px;
  }
  .contact-list__icon {
    flex: none; width: 11px; height: 11px; margin-top: 2px;
    fill: var(--note-text);
  }
</style>
</head>
<body>
  <section class="card card--front" aria-label="Business card front">
    <div class="brand">
      <div class="brand__name">Northgate HR</div>
      <div class="brand__tagline">Guide People · Reduce Risk · Build Steady Teams</div>
    </div>
    <div class="greeting">
      <svg class="greeting__bubble" viewBox="0 0 537 150" aria-hidden="true">
        <path d="M8 0 H529 a8 8 0 0 1 8 8 V132 a8 8 0 0 1 -8 8 H110 L108 183 L55 140 H8 a8 8 0 0 1 -8 -8 V8 a8 8 0 0 1 8 -8 Z" fill="var(--bubble-blue)"/>
      </svg>
      <p class="greeting__text">Hello, nice to meet you!</p>
    </div>
    <div class="holder">
      <h1 class="holder__name">Mara T. Vollen</h1>
      <p class="holder__credentials">J.D., LL.M.</p>
    </div>
  </section>

  <section class="card card--back" aria-label="Business card back">
    <div class="mark-ghost" aria-hidden="true"></div>
    <div class="contact-note">
      <svg class="contact-note__sheet" viewBox="0 0 285 285" aria-hidden="true">
        <path d="M0 0 H285 V220 L220 285 H0 Z" fill="var(--bubble-blue)"/>
        <path d="M220 285 L236 236 L285 220 Z" fill="var(--bubble-blue-dark)"/>
        <path d="M236 236 Q262 232 285 220 Q262 258 220 285 Q232 262 236 236 Z" fill="var(--paper)"/>
      </svg>
      <div class="contact-note__body">
        <h2 class="contact-note__title">Get in touch</h2>
        <ul class="contact-list">
          <li>
            <svg class="contact-list__icon" viewBox="0 0 12 12" aria-hidden="true"><path d="M6 0a4 4 0 0 0-4 4c0 3 4 8 4 8s4-5 4-8a4 4 0 0 0-4-4zm0 5.6A1.6 1.6 0 1 1 6 2.4a1.6 1.6 0 0 1 0 3.2z"/></svg>
            <span>485 E. Callister Lane<br>Maple Hollow, Florida 32804</span>
          </li>
          <li>
            <svg class="contact-list__icon" viewBox="0 0 12 12" aria-hidden="true"><path d="M0 2h12v8H0z"/><path d="M0.5 2.5l5.5 4 5.5-4" fill="none" stroke="var(--bubble-blue)" stroke-width="1"/></svg>
            <span>maravollenjd@quillpost.example</span>
          </li>
          <li>
            <svg class="contact-list__icon" viewBox="0 0 12 12" aria-hidden="true"><path d="M2.5 0.5l2 2.6-1.2 1.4c.8 1.7 2.1 3 3.8 3.8l1.4-1.2 2.6 2-1.3 2.4C4.8 11.3.7 7.2.2 1.8z"/></svg>
            <span>407-555-0183</span>
          </li>
        </ul>
      </div>
    </div>
  </section>
</body>
</html>
```